HVL Regal Business Card Design 2020

Harbor Vale Living is looking for a business card that is clean and straight to the point but still looks high-end and attractive. We are a team comprised of management and field professionals focused on the high-end residential marketplace. We serve homeowners and trade professionals directly based out of the Metrowest/Boston area. We provide client services as well as construction/renovation services.
We are aiming for a black and white feel (white background and black text) and a matte finish with rounded edges.

We want to emphasis our vision of "Properties - Projects - Partners".
Dana Pritchell is the president of HVL

Please include the following areas we service: Boston/Cape/Newport
Please make sure to include Dana's mobile (617) 555 0143 & office number (617) 555 0187, email dana@harborvaleliving.example and website www.harborvaleliving.example

Colors

Designer to choose only greyscale colors for use in the design.

Requirements
Must have
• Include "Properties - Projects - Partners" in design

Include "After Hours Emergency Support # 1800 555 0199" with icon

```html
<!DOCTYPE html>
<html lang="en">
<head>
<meta charset="utf-8">
<title>HVL Business Card</title>
<link href="https://fonts.googleapis.com/css2?family=Poppins:wght@400;500;700;800&display=swap" rel="stylesheet">
<style>
  :root {
    --stage: #2a2a2c;
    --card-dark: #1f1f21;
    --card-light: #ffffff;
    --ink: #1e1e1e;
    --ink-soft: #2b2b2b;
    --silver: #d9d9d9;
    --band: #262627;
    --band-text: #f2f2f2;
  }
  * { margin: 0; padding: 0; box-sizing: border-box; }
  html, body { width: 1200px; height: 1200px; overflow: hidden; }
  body {
    background: var(--stage);
    font-family: "Poppins", sans-serif;
    display: flex;
    flex-direction: column;
    align-items: center;
    justify-content: center;
    gap: 60px;
  }
  .card {
    width: 860px;
    height: 491px;
    position: relative;
    overflow: hidden;
  }
  /* Back side */
  .card--back {
    background: var(--card-dark);
    color: var(--silver);
    display: flex;
    flex-direction: column;
    align-items: center;
    justify-content: center;
  }
  .back-mark {
    font-weight: 800;
    font-size: 150px;
    line-height: 1;
    letter-spacing: -4px;
    color: var(--silver);
  }
  .back-name {
    font-weight: 800;
    font-size: 26px;
    letter-spacing: 5px;
    text-transform: uppercase;
    color: var(--silver);
    margin-top: 6px;
  }
  .vision {
    font-weight: 400;
    font-size: 24px;
    letter-spacing: 4px;
    text-transform: uppercase;
    color: var(--silver);
    margin-top: 22px;
  }
  /* Front side */
  .card--front {
    background: var(--card-light);
    color: var(--ink);
  }
  .front-brand {
    position: absolute;
    left: 30px;
    top: 95px;
    width: 380px;
    text-align: center;
    color: var(--ink);
    font-weight: 800;
  }
  .front-mark {
    font-size: 150px;
    line-height: 1;
    letter-spacing: -4px;
  }
  .front-name {
    font-size: 24px;
    letter-spacing: 3px;
    text-transform: uppercase;
    margin-top: 4px;
  }
  .divider {
    position: absolute;
    left: 430px;
    top: 70px;
    width: 2px;
    height: 250px;
    background: var(--ink);
  }
  .contact {
    position: absolute;
    left: 458px;
    top: 80px;
    right: 24px;
    color: var(--ink);
  }
  .contact__name {
    font-weight: 800;
    font-size: 30px;
    letter-spacing: 1.5px;
    text-transform: uppercase;
    line-height: 1.1;
  }
  .contact__title {
    font-weight: 500;
    font-size: 21px;
    margin-bottom: 20px;
  }
  .contact__list { list-style: none; }
  .contact__item {
    display: flex;
    align-items: center;
    gap: 12px;
    font-size: 19px;
    line-height: 1.55;
    color: var(--ink-soft);
    white-space: nowrap;
  }
  .contact__item svg { width: 20px; height: 20px; flex: none; }
  .service-band {
    position: absolute;
    left: 0;
    right: 0;
    top: 350px;
    height: 68px;
    background: var(--band);
    color: var(--band-text);
    display: flex;
    align-items: center;
    padding-left: 40px;
    font-weight: 500;
    font-size: 26px;
    letter-spacing: 2.5px;
  }
  .emergency {
    position: absolute;
    left: 0;
    right: 0;
    top: 418px;
    height: 73px;
    display: flex;
    align-items: center;
    justify-content: center;
    gap: 12px;
    font-weight: 500;
    font-size: 19px;
    color: var(--ink);
  }
  .emergency svg { width: 22px; height: 22px; flex: none; }
</style>
</head>
<body>

  <section class="card card--back" aria-label="Card back">
    <div class="back-mark">HVL</div>
    <div class="back-name">Harbor Vale Living</div>
    <div class="vision">Properties - Projects - Partners</div>
  </section>

  <section class="card card--front" aria-label="Card front">
    <div class="front-brand">
      <div class="front-mark">HVL</div>
      <div class="front-name">Harbor Vale Living</div>
    </div>

    <div class="divider"></div>

    <div class="contact">
      <div class="contact__name">Dana Pritchell</div>
      <div class="contact__title">President of HVL</div>
      <ul class="contact__list">
        <li class="contact__item">
          <svg viewBox="0 0 20 20" aria-hidden="true"><rect x="4" y="2" width="12" height="16" rx="1.5" fill="none" stroke="#1e1e1e" stroke-width="1.8"/></svg>
          (617) 555 0143
        </li>
        <li class="contact__item">
          <svg viewBox="0 0 20 20" aria-hidden="true"><path d="M2 7c0-3 4-4 8-4s8 1 8 4l-3 1-1-2H6L5 8z M5 10h10l2 7H3z" fill="#1e1e1e"/></svg>
          (617) 555 0187
        </li>
        <li class="contact__item">
          <svg viewBox="0 0 20 20" aria-hidden="true"><rect x="2" y="4" width="16" height="12" fill="#1e1e1e"/><path d="M2 4l8 7 8-7" fill="none" stroke="#fff" stroke-width="1.4"/></svg>
          dana@harborvaleliving.example
        </li>
        <li class="contact__item">
          <svg viewBox="0 0 20 20" aria-hidden="true"><circle cx="10" cy="10" r="8" fill="#444"/><path d="M2 10h16M10 2c-4 4-4 12 0 16M10 2c4 4 4 12 0 16" fill="none" stroke="#fff" stroke-width="1"/></svg>
          www.harborvaleliving.example
        </li>
      </ul>
    </div>

    <div class="service-band">Boston | Metrowest | South Shore | Cape | Newport</div>

    <div class="emergency">
      <svg viewBox="0 0 20 20" aria-hidden="true"><path d="M5 2l3 3-2 3c1 2 3 4 5 5l3-2 3 3-2 3C9 18 2 11 2 4z" fill="#1e1e1e"/></svg>
      After Hours Emergency Support # 1800 555 0199
    </div>
  </section>

</body>
</html>
```